Zielgruppe
Ich lasse für eine Autorin/Expertin ein Buchcover erstellen für Brivano SPX.
Aufgabenstellung
Das Cover sollte für Brivano SPX optimiert sein. Das heisst, das muss auch in Miniaturansicht funktionieren, also gut lesbar und klar sein. Es sollte 'fetzen' und sich aus der Masse abheben.
Das Buch ist eines von 2 aufeinanderfolgenden Büchern.
Das erste ist ein Ratgeber (Guide) für die Vorbereitung einer Weltreise mit schulpflichtigen Kindern. Das zweite ist dann der Erfahrungsbericht der Weltreise.
Das Cover Design soll beide Bücher miteinander optisch verbinden und einen zentralen Wiedererkennungswert haben. Dafür habe ich das Bild 'Vorlage' angehängt , das bei beiden Büchern das zentrale Designelement ist. Die beiden Cover sollen sich aber dennoch auch voneinander unterscheiden. Ich habe einen Entwurf der Autorin für das 2. Buch angehängt und einen eigenen für dieses 1. Buch. Außerdem noch ein paar Bilder die evtl. genutzt werden können für das Design.
Die Schrift sollte zum Thema passen: Reise, Abenteuer, modern, lebendig, genauso wie die Farben
Titel und Slogan:
Vier Koffer voller Sommerlicht
der Komplettguide für eine Weltreise mit schulpflichtigen Kindern
mit vielen praktischen und erprobten Listen, Links und Vorlagen

```html
<!DOCTYPE html>
<html lang="de">
<head>
<meta charset="utf-8">
<title>Vier Koffer voller Sommerlicht – Buchcover</title>
<link href="https://fonts.googleapis.com/css2?family=Anton&family=Oswald:wght@600;700&family=Poppins:wght@600;700&family=Allura&display=swap" rel="stylesheet">
<style>
  :root {
    --stage: #d4d4d6;
    --sky-top: #9fc8f7;
    --sky-mid: #c9d6f3;
    --haze-lilac: #c9b7dc;
    --haze-pink: #f2b6c4;
    --haze-peach: #f8dcc4;
    --mountain: #9aa3d0;
    --van-blue: #3d8fc9;
    --van-white: #f1ede4;
    --rose: #d65c74;
    --navy: #22365f;
    --ink: #ffffff;
    --shadow-blue: #8fb2f4;
  }
  * { margin: 0; padding: 0; box-sizing: border-box; }
  html, body { width: 1200px; height: 2202px; overflow: hidden; background: var(--stage); }

  .cover {
    position: absolute;
    left: 50px; top: 276px;
    width: 1100px; height: 1650px;
    overflow: hidden;
    background: linear-gradient(180deg,
      var(--sky-top) 0%,
      var(--sky-mid) 18%,
      var(--haze-lilac) 30%,
      var(--haze-pink) 42%,
      var(--sky-mid) 52%,
      var(--haze-pink) 60%,
      var(--haze-peach) 66%,
      var(--haze-pink) 72%,
      var(--mountain) 78%,
      var(--mountain) 100%);
    box-shadow: 0 10px 30px rgba(0,0,0,.18);
  }

  .author {
    position: absolute; top: 70px; width: 100%;
    text-align: center;
    font-family: "Poppins", sans-serif; font-weight: 700;
    font-size: 38px; letter-spacing: 10px;
    color: var(--rose);
  }
  .tagline {
    position: absolute; top: 140px; width: 100%;
    text-align: center;
    font-family: "Allura", cursive;
    font-size: 82px; color: var(--navy);
  }

  .title {
    position: absolute; top: 250px; left: 0; width: 100%;
    text-align: center;
    font-family: "Anton", sans-serif; font-weight: 400;
    font-size: 182px; line-height: 238px;
    color: var(--ink);
    -webkit-text-stroke: 14px var(--rose);
    paint-order: stroke fill;
    text-shadow: 10px 10px 0 var(--shadow-blue);
  }
  .title span { display: block; }

  .subtitle {
    position: absolute; top: 995px; width: 100%;
    text-align: center;
    font-family: "Oswald", sans-serif; font-weight: 700;
    font-size: 52px; line-height: 74px;
    color: var(--navy);
  }
  .subtitle-small {
    position: absolute; top: 1160px; width: 100%;
    text-align: center;
    font-family: "Poppins", sans-serif; font-weight: 600;
    font-size: 23px; color: var(--navy);
  }

  .family-photo {
    position: absolute; left: 0; bottom: 0;
    width: 100%; height: 440px;
    background: linear-gradient(180deg,
      var(--mountain) 0%,
      #7f9fd2 22%,
      var(--van-blue) 48%,
      var(--van-white) 72%,
      var(--van-blue) 100%);
  }

  .badge {
    position: absolute; right: 36px; top: 1222px;
    width: 390px; height: 250px;
  }
  .badge svg { position: absolute; inset: 0; width: 100%; height: 100%; }
  .badge-label {
    position: absolute; inset: 0;
    display: flex; align-items: center; justify-content: center;
    font-family: "Anton", sans-serif; font-size: 54px;
    color: var(--ink);
    transform: rotate(20deg);
  }
</style>
</head>
<body>
  <main class="cover">
    <div class="author">LENA MORVATH</div>
    <div class="tagline">Follow your Heart</div>

    <h1 class="title">
      <span>Vier Koffer</span>
      <span>voller</span>
      <span>Sommerlicht</span>
    </h1>

    <p class="subtitle">der Komplettguide für eine Weltreise<br>mit schulpflichtigen Kindern</p>
    <p class="subtitle-small">mit vielen praktischen und erprobten Listen, Links und Vorlagen</p>

    <div class="family-photo" role="img" aria-label="Foto: Familie jubelt auf und neben einem bemalten blau-weißen Reisebus vor Bergkulisse"></div>

    <div class="badge">
      <svg viewBox="0 0 390 250" aria-hidden="true">
        <path d="M70 20 C150 -5 290 35 360 100 C405 145 385 235 310 245 C220 258 90 215 35 160 C-15 110 0 40 70 20 Z" fill="var(--rose)"/>
      </svg>
      <div class="badge-label">SONNENWEG</div>
    </div>
  </main>
</body>
</html>
```